Review/Re-Design Supermarket E-Commerce website

We have launched our Supermarket E-commerce Website but feel it is lacking a modern feel.

Please re-design the current Supermarket E-commerce site, creating a more modern look and feel.

I am looking for design changes to things such as:

- Fonts
- Button shape & Size
- Shapes of boxes
- Layout of drop down menus
- A new shopping cart / button
- The Header (and in particular the use and positioning of the logo)
- Supplying a generic background image (currently berries)

Please do not change the structure of the page. For instance, the category selection will always be on the left, the items will always be displayed in rows of 3 and the shopping cart should be on the right.
Updates

Current site can be found at www.korvamarketplace.com.au

Project Deadline Extended
Reason: designs coming in are generally too different from current design. we are looking for less that 10% change to the overall look and feel. one aspect that needs a lot of work is the checkout cart on the right hand side. please checkout http://www2.pellingtonfresh.com.au/?gclid=XQWB4pzrhnLDGAKUrTmeYbNVsP

Target Market(s)

Consumers buying their weekly grocery shopping online

Industry/Entity Type

Shopping

Number of Pages Required

1 page

Requirements
Must have
• Stick to the branding of the Logo. Which is Red, Blue and White.
• Other colours may be used in small percentages.
Should not have
• Do not change the Structure of the site.

```html
<!DOCTYPE html>
<html lang="en">
<head>
<meta charset="utf-8">
<title>Korva Marketplace – Apples</title>
<link rel="stylesheet" href="https://fonts.googleapis.com/css2?family=Open+Sans:ital,wght@0,400;0,600;0,700;1,400&display=swap">
<style>
:root{
  --brand-blue:#1f5fa8;
  --brand-red:#e3262e;
  --green:#8ab547;
  --green-dark:#79a33a;
  --text:#3c4349;
  --muted:#8a9299;
  --line:#e1e4e7;
  --header-bg:#f4f5f6;
  --panel-bg:#f2f3f4;
  --pill:#e2e4e6;
  --search-btn:#a9b3bc;
}
*{box-sizing:border-box;margin:0;padding:0}
html,body{width:1200px;height:900px;overflow:hidden}
body{font-family:"Open Sans",Arial,sans-serif;color:var(--text);position:relative;background:#2b2824}
.backdrop{position:absolute;top:0;bottom:0;width:70px}
.backdrop-left{left:0;background:linear-gradient(180deg,#7a4a32 0%,#b86d3c 20%,#6c6a5e 45%,#514a42 70%,#2a2a2c 100%)}
.backdrop-right{right:0;width:68px;background:linear-gradient(180deg,#a48564 0%,#d8c3a0 25%,#6e3b2c 55%,#3b312b 80%,#1f1f22 100%)}
.page{position:absolute;left:68px;top:0;width:1065px;height:900px;background:#fff}
.site-header{position:absolute;left:0;top:0;width:100%;height:167px;background:var(--header-bg);border-bottom:1px solid #dcdfe2}
.brand{position:absolute;left:69px;top:34px;display:flex;align-items:center;gap:10px}
.brand-dot{width:30px;height:30px;border-radius:50%;background:var(--brand-red)}
.brand-name{font-size:22px;font-weight:700;color:var(--brand-blue);letter-spacing:.5px}
.main-nav{position:absolute;right:64px;top:33px;display:flex;align-items:center;gap:26px;font-size:13px}
.main-nav a{color:var(--text);text-decoration:none}
.main-nav .register{border:1px solid var(--brand-blue);color:var(--brand-blue);border-radius:4px;padding:5px 11px}
.support{position:absolute;left:69px;top:97px}
.support-label{font-size:10px;color:#a3a9ae;margin-left:2px}
.support-phone{margin-top:4px;width:153px;height:33px;border-radius:4px;background:var(--pill);display:flex;align-items:center;gap:12px;padding-left:12px;font-size:15px;font-weight:600;color:#7d858c}
.search{position:absolute;left:262px;top:113px;width:589px;height:33px;border:1px solid #cfd4d8;border-radius:4px;background:#fff;display:flex;overflow:hidden}
.search-filter{width:73px;background:#eef0f2;border-right:1px solid #cfd4d8;font-size:12px;color:#6b737a;display:flex;align-items:center;justify-content:center;gap:5px}
.search-field{flex:1;font-size:12px;color:#6b737a;display:flex;align-items:center;padding-left:13px}
.search-btn{width:32px;background:var(--search-btn);display:flex;align-items:center;justify-content:center}
.free-basket{position:absolute;left:875px;top:104px;display:flex;align-items:center;gap:2px}
.basket-art{width:50px;height:50px;border-radius:6px;background:radial-gradient(circle at 50% 35%,#d6452f 0%,#6a9b3a 45%,#8a5a2e 75%,rgba(255,255,255,0) 76%)}
.basket-text{line-height:1.05}
.basket-text strong{display:block;color:var(--brand-red);font-size:14px;font-weight:700}
.basket-text em{color:#c22a25;font-size:11px;font-weight:600}
.sidebar{position:absolute;left:20px;top:167px;width:202px;height:733px;border-right:1px solid var(--line)}
.shortcut{position:absolute;left:16px;display:flex;align-items:center;gap:12px;font-size:14px;font-weight:600;color:#2e3338}
.shortcut-count{position:absolute;left:138px;font-size:8px;font-style:italic;color:var(--muted)}
.category-list{position:absolute;left:0;top:133px;width:201px;list-style:none;border-top:1px solid var(--line)}
.category-list>li{height:37px;border-bottom:1px solid var(--line);display:flex;align-items:center;justify-content:space-between;padding:0 16px 0 21px;font-size:12px}
.category-list>li.open{border-bottom:none}
.subcategory-list{list-style:none;padding-left:47px}
.subcategory-list li{height:36px;display:flex;align-items:center;font-size:12px}
.subcategory-list li.active{font-weight:700}
.breadcrumb{position:absolute;left:253px;top:199px;font-size:12px;color:var(--muted)}
.breadcrumb .current{color:var(--text)}
.breadcrumb .sep{margin:0 6px;color:#b9bfc4}
.sort{position:absolute;left:721px;top:199px;font-size:12px}
.sort span{color:#a6b4c2}
.product{position:absolute;width:178px;height:272px;border:1px solid #dde1e4;border-radius:3px;background:#fff}
.product-photo{position:absolute;left:34px;top:16px;width:110px;height:110px;border-radius:50%}
.product-name{position:absolute;left:0;right:0;top:140px;text-align:center;font-size:12px;line-height:18px}
.qty{position:absolute;right:13px;top:208px;display:flex;align-items:center;gap:9px;font-size:11px;color:var(--muted)}
.qty i{width:10px;height:10px;border-radius:50%;background:#a8b0b6;position:relative;display:block}
.qty i::before{content:"";position:absolute;left:2px;right:2px;top:4.5px;height:1px;background:#fff}
.qty i.plus::after{content:"";position:absolute;top:2px;bottom:2px;left:4.5px;width:1px;background:#fff}
.price{position:absolute;left:16px;top:226px;font-size:15px;font-weight:600;line-height:17px}
.price small{display:block;font-size:10px;font-style:italic;font-weight:400;color:var(--muted)}
.price.special{top:228px;color:var(--brand-red)}
.price.special small{text-decoration:line-through}
.add-btn{position:absolute;right:13px;top:231px;width:59px;height:28px;border-radius:3px;background:var(--green);border:1px solid var(--green-dark);color:#fff;font-size:12px;display:flex;align-items:center;justify-content:center}
.less-tag{position:absolute;left:17px;top:206px;background:var(--green);color:#fff;font-size:9px;padding:1px 4px;border-radius:2px}
.added-bar{position:absolute;left:-1px;right:-1px;top:-1px;height:18px;background:var(--green);color:#fff;font-size:10px;display:flex;align-items:center;justify-content:center;gap:5px;border-radius:3px 3px 0 0}
.save-badge{position:absolute;left:-10px;top:-9px;width:42px;height:42px;border-radius:50%;background:var(--green);color:#fff;font-size:9px;font-weight:700;line-height:10px;display:flex;flex-direction:column;align-items:center;justify-content:center}
.cart{position:absolute;left:849px;top:233px;width:199px;border:1px solid #dcdfe2;border-radius:3px;overflow:hidden;background:var(--panel-bg)}
.cart-head{height:40px;background:#8cbb4a;color:#fff;font-size:13px;display:flex;align-items:center;gap:12px;padding-left:16px}
.cart-body{height:191px;position:relative;border-bottom:1px solid #d6dadd}
.pickup{position:absolute;left:24px;top:17px;display:flex;gap:14px}
.pickup-title{font-size:14px;color:#3c4349}
.pickup-address{font-size:8px;color:var(--muted);line-height:10px}
.delivery{position:absolute;left:40px;top:104px;display:flex;align-items:center;gap:3px;font-size:14px}
.subtotal{position:absolute;left:0;right:0;top:136px;border-top:1px solid #d9dde0;margin:0 30px;padding-top:12px;text-align:center;font-size:12px}
.subtotal strong{font-size:15px;margin-left:4px}
.checkout-btn{position:absolute;left:19px;top:182px;width:162px;height:32px;background:var(--green);border-radius:2px;color:#fff;font-size:12px;display:flex;align-items:center;justify-content:center}
.cart-body{height:230px}
.cart-item{height:64px;border-bottom:1px solid #dcdfe2;background:#f5f6f7;display:flex;justify-content:space-between;padding:12px 18px 0 19px;font-size:12px;line-height:18px}
.cart-item:first-of-type{background:#e9ebed}
.cart-item:last-child{border-bottom:none}
.cart-item-price{text-align:right;font-weight:600;font-size:13px}
.cart-item-price small{display:block;font-weight:400;font-size:8px;color:var(--muted);line-height:12px}
</style>
</head>
<body>
<div class="backdrop backdrop-left" role="img" aria-label="Background photo of fresh produce, bread and pantry foods"></div>
<div class="backdrop backdrop-right" role="img" aria-label="Background photo of baked goods and sausages"></div>

<div class="page">
  <header class="site-header">
    <div class="brand"><span class="brand-dot"></span><span class="brand-name">KORVA MARKETPLACE</span></div>
    <nav class="main-nav">
      <a href="#">Products</a><a href="#">My Cart</a><a href="#">Login</a><a href="#" class="register">Register</a>
    </nav>
    <div class="support">
      <div class="support-label">Call for support.</div>
      <div class="support-phone">
        <svg width="18" height="18" viewBox="0 0 24 24"><path fill="#8e969d" d="M6.6 10.8a15.2 15.2 0 0 0 6.6 6.6l2.2-2.2a1 1 0 0 1 1-.25 11.4 11.4 0 0 0 3.6.57 1 1 0 0 1 1 1V20a1 1 0 0 1-1 1A17 17 0 0 1 3 4a1 1 0 0 1 1-1h3.5a1 1 0 0 1 1 1c0 1.25.2 2.45.57 3.57a1 1 0 0 1-.25 1z"/></svg>
        <span>1300 555 018</span>
      </div>
    </div>
    <div class="search">
      <div class="search-filter">Filter <svg width="7" height="5" viewBox="0 0 7 5"><path d="M.5.5l3 3 3-3" fill="none" stroke="#6b737a"/></svg></div>
      <div class="search-field">Search...</div>
      <div class="search-btn"><svg width="13" height="13" viewBox="0 0 13 13"><circle cx="5.5" cy="5.5" r="4.2" fill="none" stroke="#fff" stroke-width="1.6"/><path d="M8.6 8.6l3.4 3.4" stroke="#fff" stroke-width="1.6"/></svg></div>
    </div>
    <div class="free-basket">
      <div class="basket-art" role="img" aria-label="Basket filled with fresh vegetables"></div>
      <div class="basket-text"><strong>Get Free</strong><em>Grocerie Basket</em></div>
    </div>
  </header>

  <aside class="sidebar">
    <div class="shortcut" style="top:42px">
      <svg width="24" height="24" viewBox="0 0 24 24"><path fill="#f2b01e" d="M12 1.5l3.2 6.7 7.3 1-5.3 5.1 1.3 7.3L12 18.1l-6.5 3.5 1.3-7.3L1.5 9.2l7.3-1z"/></svg>
      Favorites
    </div>
    <span class="shortcut-count" style="top:52px">58 products</span>
    <div class="shortcut" style="top:82px">
      <svg width="24" height="24" viewBox="0 0 24 24"><path fill="#e2403a" d="M12.5 2H21a1 1 0 0 1 1 1v8.5a1 1 0 0 1-.3.7l-9.8 9.8a1 1 0 0 1-1.4 0l-8.5-8.5a1 1 0 0 1 0-1.4l9.8-9.8a1 1 0 0 1 .7-.3z"/><circle cx="17" cy="7" r="1.8" fill="#fff"/></svg>
      Online Specials
    </div>
    <ul class="category-list">
      <li>Fruit <svg width="5" height="8" viewBox="0 0 5 8"><path d="M0 0l5 4-5 4z" fill="#c3c8cc"/></svg></li>
      <li>Meat <svg width="5" height="8" viewBox="0 0 5 8"><path d="M0 0l5 4-5 4z" fill="#c3c8cc"/></svg></li>
      <li>Serviced Deli <svg width="5" height="8" viewBox="0 0 5 8"><path d="M0 0l5 4-5 4z" fill="#c3c8cc"/></svg></li>
      <li class="open">Bakery <svg width="9" height="5" viewBox="0 0 9 5"><path d="M0 0h9L4.5 5z" fill="#3c4349"/></svg></li>
    </ul>
    <ul class="subcategory-list" style="position:absolute;top:284px;left:0">
      <li>Biscuits &amp; Cookies</li>
      <li class="active">Bread Rolls Pack</li>
      <li>Bread Rolls Single</li>
      <li>Cakes</li>
      <li>Croissants</li>
      <li>Crumpets</li>
      <li>Fruit Buns &amp; Cakes</li>
      <li>Grain Bread</li>
      <li>Muffin Cakes</li>
      <li>Muffins</li>
      <li>Pikelets &amp; Pancakes</li>
      <li>Pizza Bases &amp; Pita Bread</li>
    </ul>
  </aside>

  <div class="breadcrumb">Home<span class="sep">/</span>Fruit<span class="sep">/</span><span class="current">Apples</span></div>
  <div class="sort">Sort by: <span>Alphabetical ⌄</span></div>

  <article class="product" style="left:254px;top:232px">
    <div class="save-badge"><span>Save</span><span>$5,00</span></div>
    <div class="product-photo" role="img" aria-label="Photo of a bag of red apples" style="background:radial-gradient(circle at 40% 40%,#e0303a,#a10f1d 70%,rgba(255,255,255,0) 72%)"></div>
    <div class="product-name">Apples Red<br>2kg Bag<br>third text line</div>
    <span class="less-tag">Less Than</span>
    <div class="qty"><i></i>1kg<i class="plus"></i></div>
    <div class="price special">$4,56<small>$8,39</small></div>
    <div class="add-btn">Add</div>
  </article>

  <article class="product" style="left:452px;top:232px">
    <div class="added-bar"><svg width="9" height="9" viewBox="0 0 10 10"><circle cx="5" cy="5" r="4.3" fill="none" stroke="#fff"/><path d="M3 5l1.5 1.5L7 3.8" fill="none" stroke="#fff"/></svg>Added</div>
    <div class="product-photo" role="img" aria-label="Photo of a Fuji apple" style="top:26px;left:44px;width:90px;height:90px;background:radial-gradient(circle at 40% 40%,#d8703f,#9c2a22 70%,rgba(255,255,255,0) 72%)"></div>
    <div class="product-name">Fuji Apples<br>Each</div>
    <div class="qty"><i></i>1kg<i class="plus"></i></div>
    <div class="price">$0,60<small>$0,60ea</small></div>
    <div class="add-btn">Add</div>
  </article>

  <article class="product" style="left:650px;top:232px">
    <div class="product-photo" role="img" aria-label="Photo of a rosy red apple" style="top:26px;left:44px;width:90px;height:90px;background:radial-gradient(circle at 40% 40%,#e23a4a,#a0102a 70%,rgba(255,255,255,0) 72%)"></div>
    <div class="product-name">Rosy Blush Apples<br>Each</div>
    <div class="qty"><i></i>1kg<i class="plus"></i></div>
    <div class="price">$0,60<small>$0,60ea</small></div>
    <div class="add-btn">Add</div>
  </article>

  <article class="product" style="left:254px;top:523px">
    <div class="product-photo" role="img" aria-label="Photo of a green apple with a leaf" style="top:26px;left:44px;width:90px;height:90px;background:radial-gradient(circle at 40% 40%,#7fd43a,#2d8d16 70%,rgba(255,255,255,0) 72%)"></div>
    <div class="product-name">Green Apples<br>Each</div>
    <div class="qty"><i></i>1kg<i class="plus"></i></div>
    <div class="price">$0,60<small>$0,60ea</small></div>
    <div class="add-btn">Add</div>
  </article>

  <article class="product" style="left:452px;top:523px">
    <div class="product-photo" role="img" aria-label="Photo of a Royal Gala apple" style="top:26px;left:44px;width:90px;height:90px;background:radial-gradient(circle at 40% 40%,#e8a842,#c0392a 70%,rgba(255,255,255,0) 72%)"></div>
    <div class="product-name">Royal Gala Apples<br>Each</div>
    <div class="qty"><i></i>1kg<i class="plus"></i></div>
    <div class="price">$0,60<small>$0,60ea</small></div>
    <div class="add-btn">Add</div>
  </article>

  <article class="product" style="left:650px;top:523px">
    <div class="product-photo" role="img" aria-label="Photo of a bag of yellow apples" style="background:radial-gradient(circle at 45% 45%,#e2ea57,#a6c327 70%,rgba(255,255,255,0) 72%)"></div>
    <div class="product-name">Yellow Apples 1.5kg<br>Bag</div>
    <div class="qty"><i></i>1kg<i class="plus"></i></div>
    <div class="price">$5.20<small>$5,20ea</small></div>
    <div class="add-btn">Add</div>
  </article>

  <article class="product" style="left:254px;top:822px">
    <div class="product-photo" role="img" aria-label="Photo of a golden apple" style="top:34px;left:50px;width:80px;height:80px;background:radial-gradient(circle at 40% 40%,#f2c84a,#d89a1e 70%,rgba(255,255,255,0) 72%)"></div>
  </article>

  <aside class="cart">
    <div class="cart-head">
      <svg width="20" height="18" viewBox="0 0 20 18"><path d="M1 1h3l2.2 10h10l2-7H5.3" fill="none" stroke="#4e7a1e" stroke-width="1.6"/><circle cx="7.5" cy="15" r="1.6" fill="#4e7a1e"/><circle cx="15" cy="15" r="1.6" fill="#4e7a1e"/></svg>
      3 Items in your cart
    </div>
    <div class="cart-body">
      <div class="pickup">
        <svg width="30" height="30" viewBox="0 0 30 30"><path d="M5 9h18l-1.5 18H6.5z" fill="#9aa6b2"/><path d="M10 9V6a4 4 0 0 1 8 0v3" fill="none" stroke="#9aa6b2" stroke-width="2"/><path d="M19 17l8 8-3 .5 2 3-2 1-2-3-2 2z" fill="#6c7884"/></svg>
        <div><div class="pickup-title">Click&amp;Collect</div><div class="pickup-address">4/12-18 Harlow Street<br>Brennock TAS 7290</div></div>
      </div>
      <div class="delivery">
        <svg width="26" height="20" viewBox="0 0 26 20"><rect x="1" y="3" width="14" height="10" fill="#9aa6b2"/><path d="M15 6h5l4 4v3h-9z" fill="#7d8995"/><circle cx="6" cy="15" r="2.4" fill="#6c7884"/><circle cx="19" cy="15" r="2.4" fill="#6c7884"/></svg>
        Deivery Info
      </div>
      <div class="subtotal">Subtotal:<strong>$24,98</strong></div>
      <div class="checkout-btn">Checkout</div>
    </div>
    <div class="cart-item"><span>Apples Red<br>2kg Bag</span><span class="cart-item-price">$16,78<small>quantity: 2</small></span></div>
    <div class="cart-item"><span>Green Apples<br>Each</span><span class="cart-item-price">$3,00<small>quantity: 5</small></span></div>
    <div class="cart-item"><span>Yellow Apples 1.5kg<br>Bag</span><span class="cart-item-price">$5,20</span></div>
  </aside>
</div>
</body>
</html>
```